みなせ權兵衛太鼓をモチーフに、この藤田の地を干拓した様に力強くシンプルなパッケージができたらと思います。
色は2~3色程度。文字のキーワードとして①岡山②みなせ權兵衛③どら焼きの文字を入れたいと思います。※漢字・ひらがな・ローマ字等のフォントはお任せ致します。
http://www.kasumi-sangyo.example/
※最悪、岡山はなくてもOKです。
寸法は写真添付しております。
グレー系
• 高解像度JPG (.jpg)
• イラストレーター形式 (.ai)
どら焼きの文字が有っても無くても、短縮(〜どら、〜ドラ)でもOKです。
大太鼓のイメージです。影絵的にしても面白いかもしれません。参考までに。

一番イメージに近いデザインでした!

皆様、たくさんの素敵なデザインのご提案を頂きありがとうございました。それぞれが個性ある素敵な作品ばかりで、決定するのに時間かかりました。心から感謝いたします。
また機会ございましたら何卒よろしくお願い申し上げます。

```html
<!DOCTYPE html>
<html lang="ja">
<head>
<meta charset="utf-8">
<title>みなせ權兵衛 どら焼 パッケージ</title>
<link rel="stylesheet" href="https://fonts.googleapis.com/css2?family=Yuji+Boku&family=Noto+Sans+JP:wght@500&display=swap">
<style>
  :root {
    --paper: #ffffff;
    --cream: #fbf4dc;
    --cream-deep: #f3e6b8;
    --ink: #2a1d17;
    --red: #e8473f;
    --mark: #9a9a9a;
  }
  html, body {
    margin: 0;
    padding: 0;
    width: 839px;
    height: 1200px;
    overflow: hidden;
    background: var(--paper);
  }
  .sheet {
    position: relative;
    width: 839px;
    height: 1200px;
  }
  .label {
    position: absolute;
    width: 740px;
    height: 470px;
    overflow: hidden;
  }
  .label--proof { left: 22px; top: 0; }
  .label--print { left: 48px; top: 615px; width: 716px; height: 475px; }
  .label__ground {
    position: absolute;
    inset: 0;
    background: linear-gradient(135deg, var(--cream) 0%, var(--cream-deep) 50%, var(--cream) 100%);
  }
  .label__maker {
    position: absolute;
    top: 22px;
    left: 0;
    right: 0;
    text-align: center;
    font-family: "Yuji Boku", serif;
    font-size: 46px;
    color: var(--ink);
    letter-spacing: 4px;
    margin: 0;
  }
  .label__drum {
    position: absolute;
    top: 88px;
    left: 50%;
    margin-left: -27px;
    width: 54px;
    height: 54px;
    border-radius: 50%;
    background: var(--ink);
  }
  .label__reading {
    position: absolute;
    top: 122px;
    font-family: "Noto Sans JP", sans-serif;
    font-weight: 500;
    font-size: 17px;
    color: var(--ink);
    letter-spacing: 2px;
  }
  .label__reading--dora { right: calc(50% + 38px); }
  .label__reading--yaki { left: calc(50% + 38px); }
  .label__title {
    position: absolute;
    top: 148px;
    left: 0;
    right: 0;
    text-align: center;
    font-family: "Yuji Boku", serif;
    font-size: 150px;
    line-height: 1;
    color: var(--ink);
    margin: 0;
    z-index: 2;
  }
  .label__waves {
    position: absolute;
    left: 50%;
    margin-left: -190px;
    bottom: -175px;
    width: 360px;
    height: 360px;
    border-radius: 50%;
    background: var(--red);
    z-index: 1;
  }
  .label__origin {
    position: absolute;
    top: 260px;
    right: 110px;
    width: 44px;
    height: 44px;
    background: var(--red);
    color: var(--paper);
    font-family: "Noto Sans JP", sans-serif;
    font-weight: 500;
    font-size: 14px;
    display: flex;
    align-items: center;
    justify-content: center;
    z-index: 2;
  }
  .label__shadow {
    position: absolute;
    left: 22px;
    top: 455px;
    width: 740px;
    height: 60px;
    background: radial-gradient(ellipse at 50% 30%, rgba(0,0,0,0.55) 0%, rgba(0,0,0,0.15) 45%, rgba(0,0,0,0) 72%);
  }
  .crop-marks {
    position: absolute;
    left: 0;
    top: 560px;
  }
</style>
</head>
<body>
<main class="sheet">
  <div class="label__shadow" aria-hidden="true"></div>

  <section class="label label--proof">
    <div class="label__ground" role="img" aria-label="淡いクリーム色の格子模様の地"></div>
    <p class="label__maker">みなせ權兵衛</p>
    <span class="label__reading label__reading--dora">DORA</span>
    <div class="label__drum" role="img" aria-label="大太鼓のマーク"></div>
    <span class="label__reading label__reading--yaki">YAKI</span>
    <h1 class="label__title">どら焼</h1>
    <div class="label__waves" role="img" aria-label="赤い半円の青海波模様"></div>
    <span class="label__origin">岡山</span>
  </section>

  <svg class="crop-marks" width="839" height="600" viewBox="0 0 839 600" aria-hidden="true">
    <g stroke="var(--mark)" stroke-width="1.2" fill="none">
      <path d="M48 0 V45 M0 55 H38 M30 0 V45 M0 38 H38"/>
      <path d="M764 0 V45 M801 55 H839 M782 0 V45 M801 38 H839"/>
      <path d="M48 540 V600 M0 530 H38 M30 540 V600 M0 548 H38"/>
      <path d="M764 540 V600 M801 530 H839 M782 540 V600 M801 548 H839"/>
      <path d="M406 0 V30 M406 570 V600 M0 292 H25 M814 292 H839"/>
    </g>
  </svg>

  <section class="label label--print">
    <div class="label__ground" role="img" aria-label="淡いクリーム色の格子模様の地"></div>
    <p class="label__maker">みなせ權兵衛</p>
    <span class="label__reading label__reading--dora">DORA</span>
    <div class="label__drum" role="img" aria-label="大太鼓のマーク"></div>
    <span class="label__reading label__reading--yaki">YAKI</span>
    <h2 class="label__title">どら焼</h2>
    <div class="label__waves" role="img" aria-label="赤い半円の青海波模様"></div>
    <span class="label__origin">岡山</span>
  </section>
</main>
</body>
</html>
```